SEO Tool website, Front Page, Internal Page, Reports, Control Panel

I need a redesign. Right now I have my service as a sub domain of my main site. http://trackpanel.webmoxi.net. My new domain will be www.rankgridview.net. I need a front page with a logo that matches the domain name. We need a front page and internal page design for articles and “about us” “our pricing” type pages. Next we need to design the report pages that customers access. This will include the control panel, list of reports, single domain report, multiple domain comparison report. My current system has all this but I want a new design since we are adding a lot more data to the reports. Here is a link to log into the current system. http://trackpanel.webmoxi.net/login.php?t=demo

The 2 documents are the same they are just in 2 different formats.

Target Market(s)

People that work in the SEO industry primarily building links. This will be a very techie person. There are several types of people. One is a decision maker at a large SEO marketing agency or a small agency. Another will be a work at home person that has their own clients. Another might be somebod who dose seo for a company large or small.

Industry/Entity Type

Seo

Requirements
Must have
• jqery mouseovers for main menu. It needs to look very web 2.0.
• CSS based avoid table as much as possible

```html
<!DOCTYPE html>
<html lang="en">
<head>
<meta charset="utf-8">
<title>Rank Grid View – Company Info</title>
<link href="https://fonts.googleapis.com/css2?family=Arimo:wght@400;700&display=swap" rel="stylesheet">
<style>
:root{
  --header-dark:#3a4a55;
  --header-darker:#26333b;
  --logo-ink:#c9d6db;
  --logo-dot:#3a9bd0;
  --band-top:#8fd0ee;
  --band-bottom:#3b9dd4;
  --tab-green-top:#9cc234;
  --tab-green-bottom:#5e8c12;
  --tab-active-top:#ffffff;
  --tab-active-bottom:#a9d6ee;
  --tab-active-ink:#1f5f86;
  --panel-slate:#5e8493;
  --panel-slate-dark:#4d7180;
  --label-cyan:#86e2ff;
  --button-blue:#2ea7e8;
  --testi-bg:#d5e7f0;
  --testi-title:#1d3550;
  --testi-author:#2b78b3;
  --body-ink:#2a2a2a;
  --muted-ink:#6b6b6b;
  --heading-teal:#4b7f9a;
  --sidebar-border:#cfe2ec;
  --footer-dark:#35434c;
}
*{box-sizing:border-box;margin:0;padding:0}
html,body{width:1096px;height:1200px;overflow:hidden}
body{position:relative;font-family:"Arimo",Arial,sans-serif;color:var(--body-ink);background:linear-gradient(#ffffff 240px,#f4f7f9 1100px,#dfe6ea 1148px)}
.site-header{position:absolute;left:0;top:0;width:1096px;height:140px;background:linear-gradient(90deg,var(--header-darker),var(--header-dark) 50%,var(--header-darker))}
.brand{position:absolute;left:30px;top:30px;display:flex;align-items:center;gap:20px}
.brand-dot{width:86px;height:86px;border-radius:50%;background:var(--logo-dot)}
.brand-name{font-size:52px;font-weight:400;color:var(--logo-ink);letter-spacing:3px;text-transform:uppercase}
.nav-strip{position:absolute;left:0;top:140px;width:1096px;height:46px;background:linear-gradient(#f4f6f7,#dfe5e8)}
.main-nav{position:absolute;left:12px;top:150px;display:flex;gap:2px;list-style:none}
.main-nav li{height:36px;padding:0 20px;display:flex;align-items:center;font-size:14.5px;font-weight:700;color:#fff;background:linear-gradient(var(--tab-green-top),var(--tab-green-bottom));border-radius:4px 4px 0 0;text-shadow:0 1px 0 rgba(0,0,0,.3)}
.main-nav li.active{color:var(--tab-active-ink);background:linear-gradient(var(--tab-active-top),var(--tab-active-bottom));text-shadow:none}
.search-panel{position:absolute;left:876px;top:128px;width:207px;height:52px;background:#fff;border:1px solid #d0d8dc;border-radius:3px;padding:8px 9px}
.search-row{display:flex;align-items:center;gap:4px}
.search-field{flex:1;height:19px;border:1px solid #c5ced3;border-radius:8px;display:flex;align-items:center;padding-left:5px}
.search-go{font-size:11px;font-weight:700;color:#234;border:1px solid #9aa8b0;background:linear-gradient(#fff,#dde3e6);padding:1px 4px}
.search-links{margin-top:5px;font-size:10px;color:#3b6f9a;letter-spacing:.3px}
.search-links span{color:#aaa;margin:0 4px}
.blue-band{position:absolute;left:0;top:186px;width:1096px;height:44px;background:linear-gradient(var(--band-top),var(--band-bottom))}
.sidebar{position:absolute;left:6px;top:207px;width:269px;height:908px;border:2px solid var(--sidebar-border);border-radius:12px;background:linear-gradient(#e9f5fb,#ffffff 40%,#f4f9fc)}
.signin{position:absolute;left:8px;top:14px;width:254px;height:211px;background:var(--panel-slate);border-radius:10px;padding:10px 16px;color:#fff}
.signin h2{font-size:16px;font-weight:700;letter-spacing:.5px;margin:-2px -8px 10px;padding-bottom:6px;border-bottom:1px solid var(--panel-slate-dark)}
.signin label{display:block;font-size:14px;color:var(--label-cyan);margin-bottom:3px}
.signin .field{width:224px;height:27px;background:#fff;border-radius:3px;border:1px solid #9cb;margin-bottom:9px}
.signin-actions{display:flex;align-items:center;gap:22px;margin-top:6px}
.btn-signin{font-size:12px;font-weight:700;background:var(--button-blue);padding:6px 11px;border-radius:2px}
.remember{display:flex;align-items:center;gap:6px;font-size:12px;letter-spacing:1px}
.remember i{width:13px;height:13px;background:#fff;border:1px solid #888}
.forgot{margin-top:12px;font-size:10.5px;display:flex;align-items:center;gap:5px}
.signup{position:absolute;left:2px;top:236px;width:266px;height:38px;border-radius:8px;background:linear-gradient(#8fb1be,#6e93a2);color:#fff;font-size:21px;font-weight:700;padding:6px 14px}
.testimonials{position:absolute;left:2px;top:295px;width:266px;height:321px;border-radius:8px;background:var(--testi-bg);border:1px solid #b9d1de;overflow:hidden}
.testimonials h2{height:38px;background:linear-gradient(#7d9faf,#5d8192);color:#fff;font-size:21px;font-weight:400;padding:6px 12px}
.testimonial{height:91px;padding:8px 22px 0 20px;border-bottom:1px solid #b3ccd9}
.testimonial:last-child{border:0}
.testimonial h3{font-size:12.5px;color:var(--testi-title);margin-bottom:5px}
.testimonial p{font-size:10.5px;line-height:13px;color:#555;text-align:justify}
.testimonial .author{text-align:right;font-size:12px;font-weight:700;color:var(--testi-author);margin-top:4px}
.quick-stats{position:absolute;left:2px;top:639px;width:266px;height:130px;border-radius:8px;background:linear-gradient(#eef3f5,#ffffff);padding:0 14px}
.quick-stats h2{font-size:19px;font-weight:400;color:#7b8a92;padding:5px 0 8px;border-bottom:1px solid #e1e7ea;margin:0 -14px 8px;padding-left:14px;position:relative}
.quick-stats h2 svg{position:absolute;right:14px;top:-4px}
.quick-stats p{font-size:11.5px;color:#777;line-height:19px}
.quick-stats b{color:#555}
.hero{position:absolute;left:286px;top:243px;width:798px;height:290px;border:3px solid #b6cfdd;border-radius:18px;background:linear-gradient(120deg,#f1f5f8,#dbe6ee 45%,#9fb6c8 70%,#cfdbe4)}
.content{position:absolute;left:291px;top:555px;width:785px}
.content h1,.content h2{font-size:26px;font-weight:700;color:var(--heading-teal);margin-bottom:10px}
.content h2{margin-top:45px}
.content p{font-size:13.4px;line-height:19.6px;text-align:justify;margin-bottom:20px}
.site-footer{position:absolute;left:0;top:1148px;width:1096px;height:52px;background:linear-gradient(90deg,var(--header-darker),var(--footer-dark) 50%,var(--header-darker));border-top:3px solid #5b6a74}
</style>
</head>
<body>
<header class="site-header">
  <div class="brand"><span class="brand-dot"></span><span class="brand-name">Rank Grid View</span></div>
</header>
<div class="nav-strip"></div>
<div class="blue-band"></div>
<ul class="main-nav">
  <li class="active">Company Info</li>
  <li>Our Services</li>
  <li>TrackPanel / F.A.Q.</li>
  <li>TrackPanel Pricing</li>
  <li>SEO</li>
  <li>Contact WebMoxi</li>
</ul>
<div class="search-panel">
  <div class="search-row">
    <div class="search-field"><svg width="9" height="9" viewBox="0 0 10 10"><circle cx="4" cy="4" r="3" fill="none" stroke="#999" stroke-width="1.3"/><line x1="6" y1="6" x2="9" y2="9" stroke="#999" stroke-width="1.3"/></svg></div>
    <span class="search-go">GO</span>
  </div>
  <div class="search-links">Advanced Search<span>|</span>Admin Map</div>
</div>

<aside class="sidebar">
  <form class="signin">
    <h2>SIGN IN / REGISTER</h2>
    <label>Username or email</label><div class="field"></div>
    <label>Password</label><div class="field"></div>
    <div class="signin-actions"><span class="btn-signin">Sign in</span><span class="remember"><i></i>Remember Me</span></div>
    <div class="forgot"><svg width="13" height="13" viewBox="0 0 13 13"><circle cx="6.5" cy="6.5" r="6" fill="#cfe3ee"/><circle cx="6.5" cy="6.5" r="2.5" fill="#4d7180"/></svg>Forgot Password? Forgot Username?</div>
  </form>
  <div class="signup">SIGN UP &gt;</div>
  <section class="testimonials">
    <h2>Testimonals</h2>
    <div class="testimonial"><h3>Saw In Increase In My Stats....</h3><p>Lorem ipsum dolor sit amet, consectetur adipiscing elit. Vivamus sit amet elit pellentesque odio laoreet lacinia.</p><div class="author">-Jane Doe, SampleNet.io</div></div>
    <div class="testimonial"><h3>Saw In Increase In My Stats....</h3><p>Lorem ipsum dolor sit amet, consectetur adipiscing elit. Vivamus sit amet elit pellentesque odio laoreet lacinia.</p><div class="author">-Jane Doe, SampleNet.io</div></div>
    <div class="testimonial"><h3>Saw In Increase In My Stats....</h3><p>Lorem ipsum dolor sit amet, consectetur adipiscing elit. Vivamus sit amet elit pellentesque odio laoreet lacinia.</p><div class="author">-Jane Doe, SampleNet.io</div></div>
  </section>
  <section class="quick-stats">
    <h2>Quick Stats<svg width="36" height="30" viewBox="0 0 36 30"><ellipse cx="18" cy="13" rx="16" ry="11" fill="#fff" stroke="#d5dde1"/><path d="M10 21 L8 28 L16 23" fill="#fff" stroke="#d5dde1"/></svg></h2>
    <p><b>2543 created reports</b> avaiting approval</p>
    <p><b>188 purchased reports</b> in the last 24 Hour</p>
    <p><b>53 users</b> currently online</p>
    <p><b>15.2%</b> increase in traffic this month</p>
  </section>
</aside>

<div class="hero" role="img" aria-label="Photo of two businessmen in an office reviewing a document at a laptop"></div>

<main class="content">
  <h1>Learn To Get Higher and Stay Higher...</h1>
  <p>Lorem ipsum dolor sit amet, consectetur adipiscing elit. Cras lectus est, semper id volutpat vitae, aliquet sit amet dui. Maecenas a diam vitae velit porttitor adipiscing. Curabitur enim dolor, suscipit sed mollis ut, molestie ut dui. Ut lacus leo, scelerisque quis mollis nec, condimentum in ante. Pellentesque aliquam, justo sit amet adipiscing feugiat, massa leo elementum ante, non auctor tellus lectus a ligula. Ut imperdiet rhoncus luctus. Ut sed metus id ipsum tempus dignissim vel et ipsum. Proin sapien arcu, luctus in vehicula sed, posuere in lacus. Praesent dignissim consectetur blandit. Aenean in nulla eget tellus ultrices tristique quis eget ipsum. Nam vehicula sodales arcu sit amet porttitor. In hac habitasse platea dictumst. Integer laoreet dui sit amet nibh egestas ultrices.</p>
  <p>Pellentesque ornare sagittis bibendum. Aliquam erat volutpat. Mauris pellentesque tincidunt iaculis. Proin mauris lorem, tristique sed semper in, ullamcorper ac turpis. Aliquam ac iaculis metus. Ut tempus, dui nec auctor eleifend, orci tellus aliquam orci, sit amet dictum nunc magna eu velit. Nulla a dignissim quam. Integer vitae lectus augue, at rutrum augue. Sed egestas pellentesque nibh, quis accumsan est laoreet ac. Vivamus pharetra lorem eu elit porttitor quis congue dui scelerisque. Nunc urna felis, tristique vitae eleifend venenatis, ornare a velit.</p>
  <h2>Searchly, Findora, Quixo, etc....</h2>
  <p>Lorem ipsum dolor sit amet, consectetur adipiscing elit. Cras lectus est, semper id volutpat vitae, aliquet sit amet dui. Maecenas a diam vitae velit porttitor adipiscing. Curabitur enim dolor, suscipit sed mollis ut, molestie ut dui. Ut lacus leo, scelerisque quis mollis nec, condimentum in ante. Pellentesque aliquam, justo sit amet adipiscing feugiat, massa leo elementum ante, non auctor tellus lectus a ligula. Ut imperdiet rhoncus luctus. Ut sed metus id ipsum tempus dignissim vel et ipsum. Proin sapien arcu, luctus in vehicula sed, posuere in lacus. Praesent dignissim consectetur blandit. Aenean in nulla eget tellus ultrices tristique quis eget ipsum. Nam vehicula sodales arcu sit amet porttitor. In hac habitasse platea dictumst. Integer laoreet dui sit amet nibh egestas ultrices.</p>
</main>

<footer class="site-footer"></footer>
</body>
</html>
```